Business card design needed

i am a small sized carpentry business looking to generate work in decks, pergolas, small renovations including bathroom renovations or overseeing new homes being built.

Carpentry

R K Carpentry
Marcus Ellery
0417382906
Specialize in quality decks, pergolas, small renovations including bathrooms and housing project management.
FREE QUOTES

```html
<!DOCTYPE html>
<html lang="en">
<head>
<meta charset="utf-8">
<title>R K Carpentry – Business Card</title>
<link rel="stylesheet" href="https://fonts.googleapis.com/css2?family=Architects+Daughter&family=Didact+Gothic&family=Montserrat:wght@300;700;800&display=swap">
<style>
  :root {
    --bg: #e4e5e7;
    --card: #f7f8f8;
    --blue: #1f6fb5;
    --blue-light: #4f93d0;
    --blue-deep: #145a9a;
    --ink: #5d5f62;
    --ink-soft: #8a8c8f;
  }
  * { margin: 0; padding: 0; box-sizing: border-box; }
  html, body { width: 1200px; height: 1200px; overflow: hidden; background: var(--bg); }
  .canvas {
    width: 1200px; height: 1200px;
    display: flex; flex-direction: column; align-items: center; justify-content: center;
    gap: 60px;
  }
  .card {
    width: 840px; height: 480px;
    background: var(--card);
    box-shadow: 0 6px 18px rgba(0,0,0,.18);
    display: block;
  }
  .brand { font-family: "Montserrat", sans-serif; font-weight: 800; font-size: 56px; fill: var(--ink); letter-spacing: 2px; }
  .owner { font-family: "Architects Daughter", cursive; font-size: 46px; fill: var(--blue); letter-spacing: 2px; }
  .phone { font-family: "Montserrat", sans-serif; font-weight: 300; font-size: 36px; fill: var(--ink-soft); letter-spacing: 2px; }
  .service { font-family: "Didact Gothic", sans-serif; font-size: 34px; fill: var(--blue); }
  .offer { font-family: "Montserrat", sans-serif; font-weight: 700; font-size: 31px; fill: var(--ink-soft); }
</style>
</head>
<body>
<main class="canvas">

  <svg class="card card-front" viewBox="0 0 840 480" aria-label="Front of business card">
    <defs>
      <linearGradient id="plan-tone" x1="0" y1="0" x2="1" y2="1">
        <stop offset="0" stop-color="var(--blue-deep)"/>
        <stop offset="1" stop-color="var(--blue-light)"/>
      </linearGradient>
      <clipPath id="front-edge"><rect width="840" height="480"/></clipPath>
    </defs>
    <g clip-path="url(#front-edge)">
      <g transform="rotate(22 420 240)">
        <rect class="plan-panel" x="-600" y="-700" width="2000" height="730" fill="url(#plan-tone)" role="img" aria-label="Blue architectural floor plan background"/>
        <rect class="band-stripe" x="-600" y="46" width="2000" height="16" fill="var(--blue)"/>
        <rect class="band-stripe" x="-600" y="392" width="2000" height="14" fill="var(--blue)"/>
        <rect class="plan-panel" x="-600" y="420" width="2000" height="600" fill="url(#plan-tone)" role="img" aria-label="Blue architectural floor plan background"/>
        <text class="brand" x="120" y="160">R.K. CARPENTRY</text>
        <text class="owner" x="110" y="226">MARCUS ELLERY</text>
        <text class="phone" x="96" y="282">+0 417 382 906</text>
      </g>
    </g>
  </svg>

  <svg class="card card-back" viewBox="0 0 840 480" aria-label="Back of business card">
    <defs>
      <linearGradient id="plan-tone-back" x1="0" y1="0" x2="1" y2="1">
        <stop offset="0" stop-color="var(--blue)"/>
        <stop offset="1" stop-color="var(--blue-light)"/>
      </linearGradient>
    </defs>
    <polygon class="band-stripe" points="424,0 444,0 394,480 374,480" fill="var(--blue)"/>
    <polygon class="plan-panel" points="474,0 840,0 840,480 424,480" fill="url(#plan-tone-back)" role="img" aria-label="Blue architectural floor plan of a home"/>
    <g class="services" text-anchor="middle">
      <text class="service" x="205" y="82">• Quality Decks</text>
      <text class="service" x="205" y="130">• Pergolas</text>
      <text class="service" x="205" y="178">• Small Renovations</text>
      <text class="service" x="205" y="226">• Bathroom</text>
      <text class="service" x="205" y="274">• Home Oversight</text>
      <text class="offer" x="195" y="350">FREE ESTIMATES</text>
    </g>
  </svg>

</main>
</body>
</html>
```